Quillstone Business Card

We need a business card design. We have a logo from a previous Sketchfold project and I am attaching the logo files in jpeg and photoshop.

```html
<!DOCTYPE html>
<html lang="en">
<head>
<meta charset="utf-8">
<title>Quillstone Business Card</title>
<link href="https://fonts.googleapis.com/css2?family=Roboto:wght@400;500;700&display=swap" rel="stylesheet">
<style>
  :root {
    --backdrop: #ececec;
    --charcoal: #404040;
    --paper: #f3f3f3;
    --green: #3aaa35;
    --muted: #c9c9c9;
    --white: #ffffff;
  }
  html, body {
    margin: 0;
    width: 1200px;
    height: 913px;
    overflow: hidden;
    background: var(--backdrop);
    font-family: "Roboto", Arial, sans-serif;
  }
  .canvas {
    position: relative;
    width: 1200px;
    height: 913px;
  }
  .card {
    position: absolute;
    top: 314px;
    width: 500px;
    height: 286px;
    box-shadow: 0 6px 18px rgba(0,0,0,0.12);
    overflow: hidden;
  }
  .card--front { left: 80px; }
  .card--back { left: 620px; background: var(--charcoal); }
  .card__art { position: absolute; inset: 0; }
  .wordmark {
    position: absolute;
    display: flex;
    align-items: center;
    gap: 10px;
    font-weight: 700;
    letter-spacing: -0.5px;
  }
  .wordmark__square {
    width: 22px;
    height: 22px;
  }
  .card--front .wordmark {
    left: 34px;
    top: 34px;
    font-size: 36px;
    color: var(--charcoal);
  }
  .card--front .wordmark__square { background: var(--green); }
  .card--back .wordmark {
    left: 50%;
    top: 50%;
    transform: translate(-50%, -50%);
    font-size: 38px;
    color: var(--white);
  }
  .card--back .wordmark__square { background: var(--green); }
  .contact {
    position: absolute;
    left: 22px;
    top: 148px;
    margin: 0;
    padding: 0;
    list-style: none;
    font-size: 10.5px;
    line-height: 15px;
    color: var(--muted);
  }
  .contact__item {
    display: flex;
    align-items: center;
    gap: 6px;
    height: 15px;
  }
  .contact__item--plain { padding-left: 16px; }
  .contact__icon { width: 10px; height: 10px; flex: none; }
  .holder {
    position: absolute;
    right: 28px;
    top: 218px;
    text-align: right;
  }
  .holder__name {
    margin: 0;
    font-size: 15px;
    font-weight: 700;
    color: var(--green);
  }
  .holder__role {
    margin: 3px 0 0;
    font-size: 10.5px;
    color: var(--muted);
  }
</style>
</head>
<body>
<main class="canvas">
  <section class="card card--front" aria-label="Business card front">
    <svg class="card__art" viewBox="0 0 500 286" width="500" height="286">
      <rect width="500" height="286" fill="var(--paper)"/>
      <polygon points="0,100 500,190 500,286 0,286" fill="var(--charcoal)"/>
      <line x1="0" y1="100" x2="500" y2="190" stroke="var(--green)" stroke-width="3"/>
      <polygon points="420,175 450,181 432,194" fill="var(--green)"/>
    </svg>
    <div class="wordmark"><span class="wordmark__square"></span>Quillstone</div>
    <ul class="contact">
      <li class="contact__item contact__item--plain">12 Harbour Lane, Westbury, Qld 4170</li>
      <li class="contact__item contact__item--plain">Po Box 318, Eastvale.</li>
      <li class="contact__item">
        <svg class="contact__icon" viewBox="0 0 10 10"><circle cx="5" cy="5" r="5" fill="var(--green)"/><path d="M3.2 2.6 L4.2 3.8 L3.8 4.4 Q4.6 5.6 5.6 6.2 L6.2 5.8 L7.4 6.8 L6.8 7.6 Q4.2 7.2 2.4 3.4 Z" fill="var(--charcoal)"/></svg>
        08 5550 1942
      </li>
      <li class="contact__item">
        <svg class="contact__icon" viewBox="0 0 10 10"><circle cx="5" cy="5" r="5" fill="var(--green)"/><rect x="2.5" y="3.2" width="5" height="3.6" fill="none" stroke="var(--charcoal)" stroke-width="0.8"/><path d="M2.5 3.2 L5 5.2 L7.5 3.2" fill="none" stroke="var(--charcoal)" stroke-width="0.8"/></svg>
        mark@quillstone.com
      </li>
      <li class="contact__item">
        <svg class="contact__icon" viewBox="0 0 10 10"><circle cx="5" cy="5" r="5" fill="var(--green)"/><circle cx="5" cy="5" r="2.6" fill="none" stroke="var(--charcoal)" stroke-width="0.8"/><line x1="2.4" y1="5" x2="7.6" y2="5" stroke="var(--charcoal)" stroke-width="0.7"/></svg>
        www.quillstone.com
      </li>
    </ul>
    <div class="holder">
      <p class="holder__name">Mark Delaney</p>
      <p class="holder__role">Managing Director</p>
    </div>
  </section>

  <section class="card card--back" aria-label="Business card back">
    <div class="wordmark"><span class="wordmark__square"></span>Quillstone</div>
  </section>
</main>
</body>
</html>
```